Brighter Mornings Ahead book cover

I need a wonderful eye catching book cover - a modern look that hopefully represents emotions on the front page, like a string of emojis and vanishing kind of disappearing text. back cover should be totally normal since it is very text rich. Please ask me if you want me to clarify anything, I am here to help you out in any way I can, but design isn't really my thing, I just want the design of the book cover to represent my ideas in picture. See attachments for more instructions and actual text.

Target Market(s)

Adults

Font styles to use
Serif

Requirements
Must have
• Represent emotions graphically. I figured emojis could be very useful here. If you can show progression of emotions from most miserable to happiest ever in any other way, please go ahead.
• To see what type of emojis I like please view gizmo saga trailer on ViewNest. They are very modern looking and life like.
• the placement of stuff should be in this order:
• Title
• Subtitle
• Emojis
• Vanishing text
• name
Nice to have
• I want people to be attracted to the book and that it makes them happy when they see it. That is why even though the book is about addictions, I want the text where I listed addictions on front cover to kind of disappear and happy emotion comes to the forefront. Book is about integrating each and every negative emotion in order for people to come out healed, without addictions and actully ahppy.
Should not have
• morbid look, dark, strict, and it shouldn't be too serious.
• Black background really bothers me, I want something livelier even though yellow looks good on black otherwise, just not for my book. I don't want people to be afraid of emotions, so no black, thank you!

```html
<!DOCTYPE html>
<html lang="en">
<head>
<meta charset="utf-8">
<title>Brighter Mornings Ahead – Cover</title>
<link rel="stylesheet" href="https://fonts.googleapis.com/css2?family=Baskervville:wght@400;700&display=swap">
<style>
  :root {
    --paper: #fdfcfb;
    --sun: #fcc33c;
    --sky: #86c4dd;
    --sky-deep: #6fb5d2;
    --face-warm: #f7a21e;
    --face-light: #fde04a;
  }
  html, body {
    margin: 0;
    padding: 0;
    overflow: hidden;
    background: var(--paper);
  }
  .cover {
    position: relative;
    width: 800px;
    height: 1200px;
    overflow: hidden;
    background: var(--paper);
    font-family: "Baskervville", "Libre Baskerville", Georgia, serif;
  }
  .title {
    position: absolute;
    left: 0;
    right: 0;
    margin: 0;
    text-align: center;
    font-weight: 400;
    line-height: 1;
  }
  .title-main {
    top: 72px;
    font-size: 176px;
    color: var(--sun);
    letter-spacing: -2px;
  }
  .title-sub {
    color: var(--sky);
    font-size: 124px;
  }
  .title-sub.line-one { top: 280px; }
  .title-sub.line-two {
    top: 408px;
    background: linear-gradient(90deg, var(--sky) 55%, rgba(134,196,221,0.55) 100%);
    -webkit-background-clip: text;
    background-clip: text;
    color: transparent;
  }
  .mood {
    position: absolute;
    border-radius: 50%;
  }
  .mood-low {
    left: 152px;
    top: 620px;
    width: 120px;
    height: 120px;
    background: radial-gradient(circle at 50% 35%, var(--face-light), var(--face-warm) 75%);
    filter: blur(5px);
    box-shadow: 0 0 30px 20px rgba(255,255,255,0.9);
  }
  .mood-high {
    left: 428px;
    top: 508px;
    width: 264px;
    height: 264px;
    background: radial-gradient(circle at 50% 30%, var(--face-light), #fbb321 55%, var(--face-warm) 85%);
    box-shadow: 0 0 0 24px rgba(255,255,255,0.85), 0 14px 22px rgba(0,0,0,0.08);
  }
  .lead {
    position: absolute;
    top: 852px;
    left: 80px;
    right: 80px;
    margin: 0;
    text-align: center;
    color: var(--sun);
    font-size: 19.5px;
    line-height: 35px;
  }
  .habit-list {
    position: absolute;
    top: 930px;
    left: 50px;
    right: 50px;
    margin: 0;
    text-align: center;
    font-size: 22px;
    line-height: 34px;
    font-weight: 700;
    color: var(--sky-deep);
  }
  .habit-list span { white-space: nowrap; }
  .fade-1 { opacity: 0.85; filter: blur(0.4px); }
  .fade-2 { opacity: 0.6; filter: blur(1px); }
  .fade-3 { opacity: 0.35; filter: blur(1.6px); }
  .fade-4 { opacity: 0.2; filter: blur(2.2px); }
  .author {
    position: absolute;
    top: 1090px;
    left: 0;
    right: 0;
    margin: 0;
    text-align: center;
    color: var(--sun);
    font-size: 52px;
    letter-spacing: 22px;
    padding-left: 22px;
    font-weight: 400;
  }
</style>
</head>
<body>
<main class="cover">
  <h1 class="title title-main">Brighter</h1>
  <p class="title title-sub line-one">Mornings</p>
  <p class="title title-sub line-two">Ahead</p>

  <div class="mood mood-low" role="img" aria-label="Small blurred sad emoji face"></div>
  <div class="mood mood-high" role="img" aria-label="Large glossy smiling emoji face with blushing cheeks"></div>

  <p class="lead">All addictions are healed in the same way by healing emotional triggers regardless of what you are addicted to:</p>

  <p class="habit-list">
    <span>alcohol,</span> <span>drugs,</span> <span class="fade-1">sugar, arguing,</span> <span class="fade-2">binge eating,</span> <span class="fade-3">cigarettes, exercise,</span><br>
    <span class="fade-1">food, sex, gambling,</span> <span class="fade-2">video games,</span> <span class="fade-3">masturbation, TV, work,</span><br>
    <span class="fade-1">plastic surgery,</span> <span class="fade-2">skin picking,</span> <span class="fade-3">road rage, gossiping, bad</span><br>
    <span class="fade-2">relationships,</span> <span class="fade-4">Internet addiction…</span>
  </p>

  <p class="author">MIRA LOVRENC</p>
</main>
</body>
</html>
```